Building Maintenance Flyer specialising in hot and silent pressure cleaning

Hi. I love this flyer. I would like something similar but with hot water pressure washing and building maintenance

Ferro Lane & Services provides high pressure steam cleaning and water blasting services throughout Brisbane and surrounding areas, covering the Industrial, Commercial, Strata and Residential property owners sectors.

FLS combining the cleaning power of heat with state-of-the-art silent equipment, accredited technicians and a steadfast commitment to the environment. We offer the best Prompt, Professional Service.

Fully Accredited & Certified Technicians
100% Satisfaction Guaranteed
We are a family owned and operated business and love what we do. No job is too big or too small and we take pride in our work.
All of our services are undertaken using industry leading equipment and, providing safe and superior results.

Our business is covered by 20 million full public liability insurance and we operate within strict health & safety guidelines, providing all our clients with complete peace of mind. Project plans and risk assessments can also be provided upon request.

BODY CORPORATES

BUILDING FAÇADE CLEANING

CAR PARKS – underground, single and multi level

DRIVE THRU

FOOD PRODUCTION FACILITIES CLEANING SANITISING

SHOPPING CENTRES

BIRD MANAGEMENT AND DECONTAMINATION

GENERAL MAINTENANCE

CONSTRUCTION CLEAN UPS

SPILL MANAGEMENT

CONCRETE CLEANING AND DEGRASING

CONCRETE SEALING

FACTORY CLEANING & CLEAN UP

ENVIRONMENTAL DECONTAMINATION OF HEAVY VEHICLES AND EQUIPMENT

SITE CLEANS AND RUBBISH REMOVAL

MANUFACTURING PLANTS

Target Market(s)

Facility Managers, Commercial and Industrial Property Owners, Property Managers, Schools, Restaurants,

Industry/Entity Type

Pressure Cleaning

Font styles to use
Sans Serif

Colors
0293ce
00a990
33a6d7
33b8a4

Requirements
Must have
• SILENT HOT WATER PRESSURE CLEANING
Runs up to 120 Degrees Celsius
SANITISING - Bin areas, outdoor areas, cafe's, restaurants, schools, drive thru's
Blue's and Greens to link in with our logo

```html
<!DOCTYPE html>
<html lang="en">
<head>
<meta charset="utf-8">
<title>Ferro Lane &amp; Services – Property Maintenance Flyer</title>
<link rel="stylesheet" href="https://fonts.googleapis.com/css2?family=Roboto:ital,wght@0,400;0,700;0,900;1,700&family=Open+Sans:wght@400;600&display=swap">
<style>
  :root{
    --page:#f1f2f4;
    --night:#141c2a;
    --brand-blue:#2f6cc4;
    --circle-blue:#4673d0;
    --ring:#c4d2f2;
    --sky:#0293ce;
    --sky-soft:#33a6d7;
    --teal:#00a990;
    --teal-soft:#33b8a4;
    --ink:#3a3a3a;
    --text:#2b2b2b;
    --white:#ffffff;
  }
  *{box-sizing:border-box;margin:0;padding:0}
  html,body{width:1200px;height:1000px;overflow:hidden;background:var(--page)}
  body{position:relative;font-family:"Open Sans",Arial,sans-serif}
  .flyer{position:absolute;left:55px;top:110px;width:1075px;height:760px;overflow:hidden;background:var(--night)}
  .flyer__backdrop,.flyer__circle{position:absolute;left:0;top:0}

  .photo{position:absolute}
  .photo--trailer{left:20px;top:60px;width:510px;height:280px;
    background:radial-gradient(ellipse 50% 50% at 50% 50%,#1f8f94 0%,#2f7380 40%,rgba(47,115,128,0.35) 70%,rgba(20,28,42,0) 100%)}
  .photo--gear{left:380px;top:345px;width:180px;height:245px;border-radius:0 90px 90px 0;
    background:linear-gradient(135deg,#d9dade 0%,#a4a7ad 55%,#c9cbcf 100%)}
  .photo--worker{left:930px;top:345px;width:145px;height:415px;border-radius:60px 60px 0 0;
    background:linear-gradient(180deg,#e2cdbd 0%,#eeeeee 24%,#2c4f8a 42%,#243f70 100%)}

  .brand{position:absolute;left:720px;top:52px;display:flex;align-items:center;gap:14px}
  .brand__dot{width:22px;height:22px;border-radius:50%;background:var(--teal)}
  .brand__name{font-family:"Roboto",sans-serif;font-weight:900;font-size:52px;line-height:1;color:var(--brand-blue);letter-spacing:1px}

  .headline{position:absolute;left:543px;top:172px;width:470px;font-family:"Roboto",sans-serif;font-weight:900;white-space:nowrap;text-align:center}
  .headline__line{display:block;color:var(--brand-blue);font-size:42px;line-height:40px}
  .headline__main{display:block;color:var(--ink);font-size:64px;line-height:62px;letter-spacing:-1px}
  .tagline{position:absolute;left:543px;top:312px;width:470px;border-top:2px solid var(--ink);border-bottom:2px solid #777;padding:6px 0;
    font-family:"Roboto",sans-serif;font-style:italic;font-weight:700;font-size:14.5px;line-height:18px;color:var(--ink);text-align:center;white-space:nowrap}

  .features{position:absolute;left:575px;top:372px;width:350px;list-style:none}
  .feature{display:flex;align-items:center;gap:18px;font-family:Arial,sans-serif;font-size:19px;color:var(--text);line-height:1.35}
  .feature + .feature{margin-top:18px}
  .feature svg{flex:0 0 40px}

  .solutions{position:absolute;left:30px;top:422px;width:460px}
  .solutions__title{margin-left:50px;font-family:"Roboto",sans-serif;font-weight:700;font-size:27px;line-height:32px;color:var(--white)}
  .solutions__brush{margin:4px 0 0 48px;width:205px;height:4px;border-radius:2px;background:var(--white)}
  .solutions__grid{margin-top:32px;display:grid;grid-template-columns:209px 209px;row-gap:22px;list-style:none}
  .service{display:flex;align-items:center;gap:15px;font-family:Arial,sans-serif;font-size:16px;line-height:1.3;color:var(--white)}
  .service svg{flex:0 0 38px}
  .seal{position:absolute;left:300px;top:398px;width:100px;height:100px;border-radius:50%;background:radial-gradient(circle,#f2f2f2 0%,#9a9da3 70%,#d6d7da 100%);border:3px solid #e8e8e8}

  .call{position:absolute;left:530px;top:665px;width:385px;height:46px;border:2px dashed var(--brand-blue);border-radius:24px;
    display:flex;align-items:center;justify-content:center;gap:8px;font-family:"Roboto",sans-serif;font-weight:900;font-size:26px;color:var(--brand-blue)}
  .contacts{position:absolute;left:535px;top:718px;display:flex;gap:24px;font-family:Arial,sans-serif;font-size:14px;color:var(--brand-blue)}
  .contacts span{display:flex;align-items:center;gap:6px}
</style>
</head>
<body>
<main class="flyer">
  <svg class="flyer__backdrop" width="1075" height="760" viewBox="0 0 1075 760" aria-hidden="true">
    <defs>
      <linearGradient id="dusk" x1="0" y1="0" x2="0" y2="1">
        <stop offset="0" stop-color="#0e1522"/><stop offset="1" stop-color="#2a3446"/>
      </linearGradient>
      <linearGradient id="sweep" x1="0" y1="0" x2="1" y2="1">
        <stop offset="0" stop-color="#2f6cc4"/><stop offset="1" stop-color="#0293ce"/>
      </linearGradient>
      <linearGradient id="shore" x1="0" y1="0" x2="1" y2="1">
        <stop offset="0" stop-color="#ffffff"/><stop offset="1" stop-color="#33b8a4"/>
      </linearGradient>
    </defs>
    <rect width="1075" height="760" fill="url(#dusk)"/>
    <path d="M560 0 C420 90 350 300 400 470 L1075 470 L1075 0 Z" fill="url(#sweep)"/>
    <path d="M600 0 C470 90 410 290 440 470 L1075 470 L1075 0 Z" fill="var(--white)"/>
    <path d="M1075 320 C1060 380 1040 420 1010 460 L1075 460 Z" fill="var(--teal-soft)"/>
    <path d="M380 470 L1075 470 L1075 760 L380 760 Z" fill="url(#shore)"/>
    <path d="M440 560 C650 620 900 570 1075 440 L1075 400 C900 530 650 580 440 530 Z" fill="var(--brand-blue)"/>
    <path d="M440 470 L1075 470 L1075 400 C890 540 660 575 440 530 Z" fill="var(--white)"/>
  </svg>

  <div class="photo photo--gear" role="img" aria-label="Brushed steel gear illustration"></div>

  <svg class="flyer__circle" width="1075" height="760" viewBox="0 0 1075 760" aria-hidden="true">
    <circle cx="245" cy="635" r="290" fill="var(--ring)" opacity="0.55"/>
    <circle cx="245" cy="635" r="272" fill="var(--white)"/>
    <circle cx="245" cy="635" r="265" fill="var(--circle-blue)"/>
  </svg>

  <div class="photo photo--trailer" role="img" aria-label="Photo of a teal water tank on a twin-axle pressure washing trailer"></div>
  <div class="photo photo--worker" role="img" aria-label="Photo of a smiling technician in blue overalls holding a wrench"></div>

  <div class="brand"><span class="brand__dot"></span><span class="brand__name">FLS</span></div>

  <h1 class="headline">
    <span class="headline__line">ALL COMMERCIAL &amp;</span>
    <span class="headline__line">INDUSTRIAL PROPERTY</span>
    <span class="headline__main">MAINTENANCE</span>
  </h1>
  <p class="tagline">Servicing Southeast's Commercial &amp; Industrial sector 24/7</p>

  <ul class="features">
    <li class="feature">
      <svg width="40" height="40" viewBox="0 0 40 40" aria-hidden="true"><circle cx="20" cy="20" r="16" fill="none" stroke="#333" stroke-width="2.5" stroke-dasharray="80 20"/><text x="20" y="24" font-size="10" font-family="Arial" font-weight="700" text-anchor="middle" fill="#333">24/7</text></svg>
      <span>We operate 24/7, 7 days a week</span>
    </li>
    <li class="feature">
      <svg width="40" height="40" viewBox="0 0 40 40" aria-hidden="true"><path d="M28 4 L16 28" stroke="#333" stroke-width="3" stroke-linecap="round"/><path d="M12 30 l-4 6 M16 31 l-2 6 M9 27 l-6 3" stroke="#333" stroke-width="2" stroke-linecap="round"/></svg>
      <span>SILENT HOT WATER pressure cleaning 120 degrees</span>
    </li>
    <li class="feature">
      <svg width="40" height="40" viewBox="0 0 40 40" aria-hidden="true"><rect x="6" y="18" width="8" height="16" fill="#333"/><path d="M16 20 h14 a3 3 0 0 1 0 6 h-2 v6 h-12 Z" fill="#333"/><circle cx="26" cy="9" r="5" fill="none" stroke="#333" stroke-width="2.5"/></svg>
      <span>COVID-19 Trained</span>
    </li>
  </ul>

  <section class="solutions">
    <h2 class="solutions__title">Solutions For:</h2>
    <div class="solutions__brush"></div>
    <ul class="solutions__grid">
      <li class="service"><svg width="38" height="38" viewBox="0 0 38 38" aria-hidden="true"><circle cx="19" cy="19" r="16" fill="none" stroke="#fff" stroke-width="2"/><circle cx="19" cy="19" r="6" fill="#fff"/></svg><span>COVID-19<br>Infection Control</span></li>
      <li class="service"><svg width="38" height="38" viewBox="0 0 38 38" aria-hidden="true"><rect x="6" y="14" width="26" height="14" rx="4" fill="#fff"/><rect x="10" y="10" width="18" height="6" rx="2" fill="#fff"/></svg><span>Common Area<br>Cleaning</span></li>
      <li class="service"><svg width="38" height="38" viewBox="0 0 38 38" aria-hidden="true"><circle cx="22" cy="15" r="9" fill="none" stroke="#fff" stroke-width="4" stroke-dasharray="5 3"/><path d="M16 20 L6 31" stroke="#fff" stroke-width="4" stroke-linecap="round"/></svg><span>Building<br>Management</span></li>
      <li class="service"><svg width="38" height="38" viewBox="0 0 38 38" aria-hidden="true"><path d="M12 14 h14 l-2 20 h-10 Z" fill="#fff"/><circle cx="19" cy="9" r="5" fill="#fff"/></svg><span>Bird waste<br>removal</span></li>
      <li class="service"><svg width="38" height="38" viewBox="0 0 38 38" aria-hidden="true"><rect x="9" y="9" width="20" height="3" fill="#fff"/><path d="M11 14 h16 l-2 20 h-12 Z" fill="#fff"/></svg><span>Bin Cleaning &amp;<br>Sanitisation</span></li>
      <li class="service"><svg width="38" height="38" viewBox="0 0 38 38" aria-hidden="true"><circle cx="19" cy="19" r="15" fill="none" stroke="#fff" stroke-width="2.5"/><path d="M9 9 L29 29" stroke="#fff" stroke-width="2.5"/></svg><span>Mould &amp;<br>Mildew removal</span></li>
      <li class="service"><svg width="38" height="38" viewBox="0 0 38 38" aria-hidden="true"><path d="M5 24 h18 l-3 8 h-12 Z" fill="#fff"/><circle cx="28" cy="30" r="3" fill="#fff"/><path d="M19 20 v-10 M19 10 c-6 0 -6 6 0 6 M19 10 c6 0 6 6 0 6" stroke="#fff" stroke-width="2" fill="none"/></svg><span>Garden<br>Maintenance</span></li>
      <li class="service"><svg width="38" height="38" viewBox="0 0 38 38" aria-hidden="true"><rect x="6" y="16" width="26" height="14" rx="2" fill="none" stroke="#fff" stroke-width="2.5"/><rect x="4" y="12" width="30" height="4" fill="#fff"/></svg><span>Oil and Grease<br>elimination</span></li>
    </ul>
  </section>
  <div class="seal" role="img" aria-label="Satisfaction guarantee seal"></div>

  <div class="call">
    <svg width="22" height="22" viewBox="0 0 24 24" aria-hidden="true"><path d="M6.6 10.8a15 15 0 0 0 6.6 6.6l2.2-2.2a1 1 0 0 1 1-.25 11.4 11.4 0 0 0 3.6.57 1 1 0 0 1 1 1V20a1 1 0 0 1-1 1A17 17 0 0 1 3 4a1 1 0 0 1 1-1h3.5a1 1 0 0 1 1 1c0 1.25.2 2.45.57 3.57a1 1 0 0 1-.25 1Z" fill="var(--brand-blue)"/></svg>
    <span>CALL NOW! 555-010-202</span>
  </div>
  <div class="contacts">
    <span><svg width="14" height="10" viewBox="0 0 14 10" aria-hidden="true"><rect width="14" height="10" fill="var(--brand-blue)"/><path d="M0 0 L7 6 L14 0" stroke="#fff" fill="none"/></svg>info@ferrolane.example</span>
    <span><svg width="13" height="13" viewBox="0 0 14 14" aria-hidden="true"><circle cx="7" cy="7" r="6.5" fill="var(--brand-blue)"/><path d="M0.5 7 H13.5 M7 0.5 C3 4 3 10 7 13.5 M7 0.5 C11 4 11 10 7 13.5" stroke="#fff" fill="none" stroke-width="1"/></svg>www.ferrolane.example</span>
  </div>
</main>
</body>
</html>
```